Fair Harbor Ripple alcohol cooler

I need a design using my Quillmere Beverage Logo for 4 different styles of Malt Beverage. The cocktails are easy drinking tropical feel. We will be using the best ingredients and try to be all natural and organic.
Tovel Lime
Tovel Orange
Tovel Grapefruit
Tovel Strawberry
We would like as few colors as possible in the design.

Target Market(s)

21 - 50
Women

Requirements
Must have
• the 4 styles
• my LOGO
• label dimension inside 3"wide x 4"high maximum
• 4 pack design
• label must have 12 FL OZ
• label must have 5% ALC/VOL
Nice to have
• Clean crisp feel
Should not have
• please keep design to 3 colors or less

```html
<!DOCTYPE html>
<html lang="en">
<head>
<meta charset="utf-8">
<title>Tovel Labels – Quillmere Beverage</title>
<link rel="stylesheet" href="https://fonts.googleapis.com/css2?family=Montserrat:wght@300;400;600&display=swap">
<style>
  :root {
    --ink: #3a3a3a;
    --ink-soft: #4a4a4a;
    --paper: #ffffff;
    --lime: #bcd435;
    --lime-deep: #8fb52a;
    --orange: #f39200;
    --orange-light: #fcd488;
    --grapefruit: #f7b592;
    --grapefruit-light: #fbd9d2;
    --strawberry: #e30613;
    --strawberry-deep: #a51f2d;
  }
  * { box-sizing: border-box; margin: 0; padding: 0; }
  html, body {
    width: 1200px;
    height: 345px;
    overflow: hidden;
    background: var(--paper);
    font-family: "Montserrat", Arial, sans-serif;
    color: var(--ink);
  }
  .label-set {
    position: relative;
    width: 1200px;
    height: 345px;
  }
  .label {
    position: absolute;
    top: 2px;
    width: 262px;
    height: 343px;
    background: var(--paper);
    box-shadow: 0 0 0 0.5px #e6e6e6;
    overflow: hidden;
  }
  .label--lime { left: 0; }
  .label--orange { left: 328px; }
  .label--grapefruit { left: 640px; }
  .label--strawberry { left: 941px; width: 259px; }

  .label__wash {
    position: absolute;
    left: 0; top: 0;
    width: 100%;
    height: 130px;
  }
  .label--lime .label__wash {
    background:
      radial-gradient(ellipse 70% 90% at 10% 10%, var(--lime) 0%, rgba(188,212,53,0) 70%),
      radial-gradient(ellipse 60% 60% at 90% 20%, rgba(143,181,42,0.55) 0%, rgba(143,181,42,0) 70%),
      linear-gradient(to bottom, rgba(188,212,53,0.5), rgba(255,255,255,0));
  }
  .label--orange .label__wash {
    background:
      radial-gradient(ellipse 60% 80% at 5% 10%, var(--orange-light) 0%, rgba(252,212,136,0) 70%),
      radial-gradient(ellipse 60% 60% at 85% 40%, rgba(250,232,160,0.8) 0%, rgba(250,232,160,0) 70%),
      linear-gradient(to bottom, rgba(252,220,140,0.55), rgba(255,255,255,0));
  }
  .label--grapefruit .label__wash {
    background:
      radial-gradient(ellipse 60% 80% at 10% 10%, var(--grapefruit-light) 0%, rgba(251,217,210,0) 70%),
      radial-gradient(ellipse 50% 60% at 95% 25%, rgba(246,200,225,0.9) 0%, rgba(246,200,225,0) 70%),
      linear-gradient(to bottom, rgba(251,215,205,0.6), rgba(255,255,255,0));
  }
  .label--strawberry .label__wash {
    background:
      radial-gradient(ellipse 70% 50% at 50% 0%, var(--strawberry-deep) 0%, rgba(165,31,45,0) 80%),
      radial-gradient(ellipse 50% 60% at 5% 30%, rgba(227,6,19,0.45) 0%, rgba(227,6,19,0) 70%),
      linear-gradient(to bottom, rgba(200,40,55,0.45), rgba(255,255,255,0));
  }

  .brand-mark {
    position: absolute;
    left: 50%;
    top: 30px;
    width: 96px;
    height: 96px;
    margin-left: -48px;
    border-radius: 50%;
    background: var(--paper);
    display: flex;
    align-items: center;
    justify-content: center;
    text-align: center;
  }
  .brand-mark__name {
    font-weight: 600;
    font-size: 10.5px;
    line-height: 1.25;
    letter-spacing: 0.8px;
    text-transform: uppercase;
    color: var(--ink);
  }

  .flavour-art {
    position: absolute;
    left: 50%;
    top: 148px;
    width: 54px;
    height: 54px;
    margin-left: -27px;
    border-radius: 50%;
  }
  .label--lime .flavour-art { background: radial-gradient(circle, #e2eda8, var(--lime)); }
  .label--orange .flavour-art { background: radial-gradient(circle, #fbe0c4, var(--orange)); }
  .label--grapefruit .flavour-art { background: radial-gradient(circle, #fde3d6, var(--grapefruit)); }
  .label--strawberry .flavour-art { background: radial-gradient(circle, #f04a40, var(--strawberry)); }

  .label__name {
    position: absolute;
    left: 0; right: 0;
    top: 219px;
    text-align: center;
    font-weight: 300;
    font-size: 21px;
    line-height: 25px;
    letter-spacing: 0.6px;
    text-transform: uppercase;
    color: var(--ink-soft);
  }
  .label__type {
    position: absolute;
    left: 0; right: 0;
    top: 278px;
    text-align: center;
    font-size: 8.5px;
    letter-spacing: 0.3px;
    text-transform: uppercase;
    color: var(--ink-soft);
  }
  .label__facts {
    position: absolute;
    left: 18px; right: 18px;
    top: 299px;
    display: flex;
    justify-content: space-between;
    font-size: 8.5px;
    letter-spacing: 0.3px;
    text-transform: uppercase;
    color: var(--ink-soft);
  }
  .label__band {
    position: absolute;
    left: 0; right: 0;
    bottom: 0;
    height: 28px;
  }
  .label--lime .label__band { background: var(--lime); }
  .label--orange .label__band { background: var(--orange); }
  .label--grapefruit .label__band { background: var(--grapefruit); }
  .label--strawberry .label__band { background: var(--strawberry); }
</style>
</head>
<body>
<main class="label-set">

  <section class="label label--lime">
    <div class="label__wash"></div>
    <div class="brand-mark"><span class="brand-mark__name">Quillmere<br>Beverage</span></div>
    <div class="flavour-art" role="img" aria-label="Lime wedge illustration"></div>
    <h2 class="label__name">Tovel<br>Lime</h2>
    <p class="label__type">Alcoholic Malt Beverage</p>
    <div class="label__facts"><span>12FL OZ</span><span>5% ALC/VOL</span></div>
    <div class="label__band"></div>
  </section>

  <section class="label label--orange">
    <div class="label__wash"></div>
    <div class="brand-mark"><span class="brand-mark__name">Quillmere<br>Beverage</span></div>
    <div class="flavour-art" role="img" aria-label="Orange wedge illustration"></div>
    <h2 class="label__name">Tovel<br>Orange</h2>
    <p class="label__type">Alcoholic Malt Beverage</p>
    <div class="label__facts"><span>12FL OZ</span><span>5% ALC/VOL</span></div>
    <div class="label__band"></div>
  </section>

  <section class="label label--grapefruit">
    <div class="label__wash"></div>
    <div class="brand-mark"><span class="brand-mark__name">Quillmere<br>Beverage</span></div>
    <div class="flavour-art" role="img" aria-label="Grapefruit wedge illustration"></div>
    <h2 class="label__name">Tovel<br>Grapefruit</h2>
    <p class="label__type">Alcoholic Malt Beverage</p>
    <div class="label__facts"><span>12FL OZ</span><span>5% ALC/VOL</span></div>
    <div class="label__band"></div>
  </section>

  <section class="label label--strawberry">
    <div class="label__wash"></div>
    <div class="brand-mark"><span class="brand-mark__name">Quillmere<br>Beverage</span></div>
    <div class="flavour-art" role="img" aria-label="Strawberry illustration"></div>
    <h2 class="label__name">Tovel<br>Strawberry</h2>
    <p class="label__type">Alcoholic Malt Beverage</p>
    <div class="label__facts"><span>12FL OZ</span><span>5% ALC/VOL</span></div>
    <div class="label__band"></div>
  </section>

</main>
</body>
</html>
```